Vitoplume.com

I need a web design for a Online Wellness Center based in Chicago, IL and it's called "Vitoplume" We provide Health risk assessment to individuals and interventions. Our portal has a Health Activity tracker where our members record health activities and aerobic miles and biometric data. Our Online wellness center tracks the participant's progress toward health goals and awards points for completed activities.
I started working on this website but the designer was not able to designer a website which describes what we do. I need a fresh look on this project. I need a very attractive, responsive website which says what we do.
These are the things we do.
1. We provide Health Risk Assessments to individuals and Co-operations
2. We Provide Free health screenings to undeserved communities
3. Assist individuals access free or affordable medications
4. We ask providers/doctors to see (or do a complete physical) one individual free of charge once a year (those individuals who are no insured and don't have money to pay from their pocket)
5. Assist patient access lab work at low cost
Our goal is to provide services that will lower the cost of care for our members.

Here is the website: www.vitoplume.com still underdevelopment. PLEASE DO NOT COPY THIS STYLE OF WEBSITE. IT'S A BAD DESIGN AND THAT IS WHY I'M RE-DESIGNING THE SITE

Target Market(s)

Health individuals between the age of 21 to 65 Plus years old. Insured and uninsured

Industry/Entity Type

Health And Wellness

Coding

Coded - Design and coding required

Number of Pages Required

5+ page

Colors
0292cd

Requirements
Must have
• I'm still working on this websiteHere is the menu: Home, About us, Services, Health Screening, Providers, Contacts
• Please see. www.vitoplume.com
Nice to have
• Event calender
• Upcoming Event
• Medication
• Lab assist
• Providers/Free Clinics

```html
<!DOCTYPE html>
<html lang="en">
<head>
<meta charset="utf-8">
<title>Vitoplume – Online Wellness Center</title>
<link href="https://fonts.googleapis.com/css2?family=Open+Sans:wght@400;600;700&display=swap" rel="stylesheet">
<style>
:root{
  --blue:#0292cd;
  --blue-dark:#0273a6;
  --blue-light:#d9ecf7;
  --band:#cfe6f4;
  --navy:#1e2a36;
  --ink:#333;
  --muted:#777;
  --grey-box:#3b3e41;
  --footer:#2c3034;
  --footer-deep:#222528;
  --white:#fff;
}
*{box-sizing:border-box;margin:0;padding:0}
html,body{width:1200px;height:2740px;overflow:hidden}
body{font-family:"Open Sans",Arial,sans-serif;color:var(--ink);background:var(--white);position:relative}
.wrap{width:940px;margin:0 auto;position:relative}
section,header,footer{position:relative;width:1200px}

/* header */
.site-header{height:145px;background:linear-gradient(180deg,#0a7fbf,#29a7de 60%,#6cc3ea)}
.brand{position:absolute;left:130px;top:22px;color:var(--white);font-size:30px;font-weight:700;letter-spacing:.3px;display:flex;align-items:center;gap:10px}
.brand-dot{width:22px;height:22px;border-radius:50%;background:var(--white)}
.phone{position:absolute;right:130px;top:28px;color:var(--white);font-size:24px;font-weight:600;display:flex;align-items:center;gap:10px}
.main-nav{position:absolute;left:130px;top:74px;width:940px;height:38px;background:var(--navy);display:flex}
.main-nav a{flex:1;color:var(--white);text-decoration:none;font-size:12px;font-weight:600;text-transform:uppercase;display:flex;align-items:center;justify-content:center;border-right:1px solid #33414f}
.main-nav a.active{background:var(--blue)}

/* hero */
.hero{height:535px;background:linear-gradient(110deg,#c9d7df 0%,#eef3f6 35%,#dfe8ee 60%,#b9cbd6 100%)}
.hero-photo{position:absolute;inset:0}
.hero-caption{position:absolute;left:160px;top:215px;width:470px;background:rgba(20,30,40,.72);color:var(--white);padding:22px 26px;font-size:22px;font-weight:600;line-height:1.45;text-transform:uppercase}

/* welcome */
.welcome{height:150px;text-align:center;padding-top:28px}
.welcome h1{font-size:34px;font-weight:600;color:#2b2b2b}
.welcome h1 span{color:var(--blue)}
.welcome p{width:940px;margin:12px auto 0;font-size:11px;line-height:1.6;color:var(--muted)}
.btn{display:inline-block;background:var(--blue);color:var(--white);font-size:11px;font-weight:700;text-transform:uppercase;padding:8px 18px;text-decoration:none}
.welcome .btn{margin-top:12px}

/* what we do */
.services{height:450px;background:linear-gradient(180deg,#e7f3fa,var(--band));padding-top:40px;text-align:center}
.section-title{font-size:34px;font-weight:600;color:#2b2b2b}
.cards{display:flex;justify-content:space-between;margin-top:30px}
.card{width:290px}
.card-photo{height:160px;border:4px solid var(--white);box-shadow:0 1px 3px rgba(0,0,0,.15)}
.card-caption{height:78px;background:var(--white);color:var(--blue);font-size:14px;font-weight:600;line-height:1.4;display:flex;align-items:center;justify-content:center;padding:0 24px;margin-top:12px}
.dots{display:flex;justify-content:center;gap:8px;margin-top:22px}
.dots i{width:14px;height:14px;border-radius:50%;border:2px solid #7aa7c2;display:block}

/* medication */
.medication{height:430px;background:#fafafa}
.med-photo{position:absolute;left:0;top:0;width:560px;height:430px;background:radial-gradient(ellipse at 60% 55%,#e9c8b2 0%,#dcb49c 35%,#f3ece7 70%,#fafafa 100%)}
.med-text{position:absolute;left:610px;top:60px;width:460px}
.med-text h2{font-size:34px;font-weight:600;color:var(--blue)}
.med-text p{margin-top:14px;font-size:11px;line-height:1.7;color:var(--muted)}

/* feature boxes */
.features{height:260px;padding-top:20px}
.features .wrap{display:flex;justify-content:space-between}
.feature{width:460px;height:220px;position:relative;color:var(--white);padding:20px 22px}
.feature.lab{background:var(--grey-box)}
.feature.clinic{background:var(--blue)}
.feature h3{font-size:28px;font-weight:400}
.feature p{width:270px;margin-top:10px;font-size:10px;line-height:1.6;color:rgba(255,255,255,.75)}
.feature .more{position:absolute;right:22px;bottom:16px;font-size:10px;font-weight:700;text-transform:uppercase}
.feature .icon{position:absolute;right:60px;top:60px}

/* events */
.events{height:400px;background:linear-gradient(180deg,#fff,#eef6fb)}
.events .wrap{display:flex;justify-content:space-between;padding-top:20px}
.upcoming{width:540px}
.upcoming h2{font-size:32px;font-weight:600;color:#2b2b2b;padding-bottom:10px;border-bottom:1px solid #dde3e8}
.event-list{display:flex;justify-content:space-between;margin-top:18px}
.event{width:260px}
.event-photo{height:120px;border:3px solid var(--white);box-shadow:0 1px 3px rgba(0,0,0,.15)}
.event h4{margin-top:10px;font-size:13px;color:var(--blue);font-weight:600}
.event .date{font-size:10px;color:#999;margin-top:2px}
.event p{font-size:10px;line-height:1.6;color:var(--muted);margin-top:6px}

.calendar{width:340px}
.cal-head{height:44px;display:flex;align-items:center;justify-content:space-between;border-bottom:1px solid #dde3e8}
.cal-head strong{font-size:22px;font-weight:400;color:#2b2b2b}
.cal-arrow{width:30px;height:30px;border-radius:50%;background:var(--blue);display:flex;align-items:center;justify-content:center}
.cal-grid{display:grid;grid-template-columns:repeat(7,1fr);margin-top:12px;font-size:12px;text-align:center}
.cal-grid span{height:38px;line-height:38px;color:#555;border-bottom:1px solid #e3e9ee}
.cal-grid .dow{color:#999;font-weight:600}
.cal-grid .we{background:var(--blue);color:var(--white);border-bottom-color:#2aa5d9}

/* footer */
.site-footer{height:370px;background:var(--footer);color:#b7bcc0}
.newsletter{height:70px;background:var(--footer-deep);display:flex;align-items:center}
.newsletter .wrap{display:flex;align-items:center;gap:20px}
.newsletter .label{color:var(--blue);font-size:15px;font-weight:600;line-height:1.2;width:260px}
.newsletter .label small{display:block;color:#9aa0a5;font-size:10px;font-weight:400}
.field{width:230px;height:32px;background:var(--white);color:#999;font-size:11px;padding:0 10px;display:flex;align-items:center}
.newsletter .btn{padding:10px 30px}
.foot-cols{display:flex;justify-content:space-between;padding-top:30px}
.foot-col{width:280px}
.foot-col h5{color:var(--blue);font-size:17px;font-weight:600;margin-bottom:14px}
.links{display:grid;grid-template-columns:1fr 1fr;gap:8px 10px;font-size:11px;list-style:none}
.links li::before{content:"› ";color:var(--blue)}
.contact-line{display:flex;align-items:center;gap:10px;font-size:11px;margin-bottom:10px}
.social{display:grid;grid-template-columns:1fr 1fr;gap:12px;font-size:11px}
.social span{display:flex;align-items:center;gap:8px}
.social i{width:26px;height:26px;border-radius:50%;background:#43494e;display:block}
.copyright{position:absolute;left:0;bottom:0;width:1200px;height:40px;background:var(--footer-deep);font-size:10px;text-align:center;line-height:40px;color:#888}
</style>
</head>
<body>

<header class="site-header">
  <div class="brand"><span class="brand-dot"></span>Vitoplume</div>
  <div class="phone">
    <svg width="22" height="22" viewBox="0 0 24 24" aria-hidden="true"><path fill="#fff" d="M6.6 10.8a15.1 15.1 0 0 0 6.6 6.6l2.2-2.2c.3-.3.7-.4 1-.2 1.1.4 2.3.6 3.6.6.6 0 1 .4 1 1V20c0 .6-.4 1-1 1A17 17 0 0 1 3 4c0-.6.4-1 1-1h3.5c.6 0 1 .4 1 1 0 1.3.2 2.5.6 3.6.1.3 0 .7-.2 1z"/></svg>
    +123 456 700
  </div>
  <nav class="main-nav">
    <a href="#" class="active">Home</a>
    <a href="#">About us</a>
    <a href="#">Services</a>
    <a href="#">Health Screening</a>
    <a href="#">Providers</a>
    <a href="#">Contacts</a>
  </nav>
</header>

<section class="hero">
  <div class="hero-photo" role="img" aria-label="Smiling pharmacist in a white coat in front of pharmacy shelves"></div>
  <div class="hero-caption">We are non profit organization whose main aim is only to make healthy USA.</div>
</section>

<section class="welcome">
  <h1>Welcome to <span>Vitoplume</span></h1>
  <p>Our online wellness center helps members record health activities, aerobic miles and biometric data, and tracks progress toward personal health goals. Every completed activity earns points, and our team offers health risk assessments, free screenings and help with medications and lab work so that care costs less for every member, insured or uninsured, across Chicago and beyond.</p>
  <a href="#" class="btn">Read more</a>
</section>

<section class="services">
  <h2 class="section-title">What we do?</h2>
  <div class="wrap cards">
    <div class="card">
      <div class="card-photo" role="img" aria-label="Doctor talking with an older patient" style="background:linear-gradient(135deg,#c7d6df,#eef2f4 55%,#b7c6cf)"></div>
      <div class="card-caption">Health Risk Assessment to individuals and Co-operations</div>
    </div>
    <div class="card">
      <div class="card-photo" role="img" aria-label="Ultrasound scan during a health screening" style="background:linear-gradient(135deg,#4d5358,#9aa1a6 55%,#5f666b)"></div>
      <div class="card-caption">Free health screenings to underserved communities</div>
    </div>
    <div class="card">
      <div class="card-photo" role="img" aria-label="Hands holding blister packs of medication" style="background:linear-gradient(135deg,#dfe6ea,#b9c7d0 55%,#e9eef1)"></div>
      <div class="card-caption">Assist individuals access free or affordable medications</div>
    </div>
  </div>
  <div class="dots"><i></i><i></i></div>
</section>

<section class="medication">
  <div class="med-photo" role="img" aria-label="Open hand holding a pile of colourful pills"></div>
  <div class="med-text">
    <h2>Medication</h2>
    <p>Many members struggle to pay for the prescriptions they need. We guide each person through assistance programs, generic options and pharmacy discounts so that treatment is never skipped because of price. Our care team reviews current prescriptions, checks eligibility for free or low cost supply and follows up until the medication is in hand. We also work with local providers who agree to see one uninsured patient free of charge once a year for a complete physical, giving families a clear picture of their health and a plan they can afford.</p>
  </div>
</section>

<section class="features">
  <div class="wrap">
    <div class="feature lab">
      <h3>Lab assist</h3>
      <p>We help patients reach partner labs for routine blood work and tests at a low cost, with results shared securely.</p>
      <svg class="icon" width="70" height="70" viewBox="0 0 70 70" aria-hidden="true"><circle cx="35" cy="35" r="32" fill="none" stroke="#6b7075" stroke-width="3"/><path d="M28 18h14M31 18v14l-10 18h28L39 32V18" fill="none" stroke="#6b7075" stroke-width="3" stroke-linejoin="round"/></svg>
      <span class="more">Read more</span>
    </div>
    <div class="feature clinic">
      <h3>Free Clinics</h3>
      <p>Find free clinics and providers near you who offer yearly check ups for members without insurance or savings.</p>
      <svg class="icon" width="70" height="70" viewBox="0 0 70 70" aria-hidden="true"><path d="M8 30 35 10l27 20v30H8z" fill="none" stroke="#8fd0ee" stroke-width="3" stroke-linejoin="round"/><path d="M35 28v22M24 39h22" stroke="#8fd0ee" stroke-width="5"/></svg>
      <span class="more">Read more</span>
    </div>
  </div>
</section>

<section class="events">
  <div class="wrap">
    <div class="upcoming">
      <h2>Upcoming Event</h2>
      <div class="event-list">
        <div class="event">
          <div class="event-photo" role="img" aria-label="Medical team standing together" style="background:linear-gradient(135deg,#e3eaee,#c4d2da 60%,#eef2f4)"></div>
          <h4>Community screening day</h4>
          <div class="date">12 September, 2015</div>
          <p>Free blood pressure, glucose and weight checks for all ages.</p>
        </div>
        <div class="event">
          <div class="event-photo" role="img" aria-label="Doctor consulting a patient" style="background:linear-gradient(135deg,#d7e2e8,#f0f3f5 55%,#b8c8d1)"></div>
          <h4>Healthy living workshop</h4>
          <div class="date">26 September, 2015</div>
          <p>Learn to track activity, set goals and earn member points.</p>
        </div>
      </div>
    </div>

    <div class="calendar">
      <div class="cal-head">
        <span class="cal-arrow"><svg width="12" height="12" viewBox="0 0 12 12" aria-hidden="true"><path d="M8 1 3 6l5 5" fill="none" stroke="#fff" stroke-width="2"/></svg></span>
        <strong>September 2015</strong>
        <span class="cal-arrow"><svg width="12" height="12" viewBox="0 0 12 12" aria-hidden="true"><path d="m4 1 5 5-5 5" fill="none" stroke="#fff" stroke-width="2"/></svg></span>
      </div>
      <div class="cal-grid">
        <span class="dow">Mo</span><span class="dow">Tu</span><span class="dow">We</span><span class="dow">Th</span><span class="dow">Fr</span><span class="dow we">Sa</span><span class="dow we">Su</span>
        <span></span><span>01</span><span>02</span><span>03</span><span>04</span><span class="we">05</span><span class="we">06</span>
        <span>07</span><span>08</span><span>09</span><span>10</span><span>11</span><span class="we">12</span><span class="we">13</span>
        <span>14</span><span>15</span><span>16</span><span>17</span><span>18</span><span class="we">19</span><span class="we">20</span>
        <span>21</span><span>22</span><span>23</span><span>24</span><span>25</span><span class="we">26</span><span class="we">27</span>
        <span>28</span><span>29</span><span>30</span><span></span><span></span><span class="we"></span><span class="we"></span>
      </div>
    </div>
  </div>
</section>

<footer class="site-footer">
  <div class="newsletter">
    <div class="wrap">
      <div class="label">Sign up to stay in touch <small>Sign up for a newsletter</small></div>
      <div class="field">Name</div>
      <div class="field">Email</div>
      <a href="#" class="btn">Sign up</a>
    </div>
  </div>
  <div class="wrap foot-cols">
    <div class="foot-col">
      <h5>Quick Links</h5>
      <ul class="links">
        <li>Home</li><li>Providers</li>
        <li>About Us</li><li>Contact Us</li>
        <li>Services</li><li>Upcoming Events</li>
        <li>Health Screening</li>
      </ul>
    </div>
    <div class="foot-col">
      <h5>Contact Us</h5>
      <div class="contact-line">
        <svg width="14" height="18" viewBox="0 0 14 18" aria-hidden="true"><path d="M7 0a7 7 0 0 0-7 7c0 5 7 11 7 11s7-6 7-11a7 7 0 0 0-7-7zm0 9.5A2.5 2.5 0 1 1 7 4.5a2.5 2.5 0 0 1 0 5z" fill="#0292cd"/></svg>
        418 Lakeview Row, Chicago IL 60611
      </div>
      <div class="contact-line">
        <svg width="14" height="14" viewBox="0 0 24 24" aria-hidden="true"><path fill="#0292cd" d="M6.6 10.8a15.1 15.1 0 0 0 6.6 6.6l2.2-2.2c.3-.3.7-.4 1-.2 1.1.4 2.3.6 3.6.6.6 0 1 .4 1 1V20c0 .6-.4 1-1 1A17 17 0 0 1 3 4c0-.6.4-1 1-1h3.5c.6 0 1 .4 1 1 0 1.3.2 2.5.6 3.6.1.3 0 .7-.2 1z"/></svg>
        +123 456 700
      </div>
      <div class="contact-line">
        <svg width="14" height="12" viewBox="0 0 14 12" aria-hidden="true"><rect x="0.5" y="0.5" width="13" height="11" fill="none" stroke="#0292cd"/><path d="m1 1 6 5 6-5" fill="none" stroke="#0292cd"/></svg>
        hello@vitoplume.com
      </div>
    </div>
    <div class="foot-col">
      <h5>Contact Us</h5>
      <div class="social">
        <span><i></i>Friends page</span><span><i></i>News feed</span>
        <span><i></i>Friends page</span><span><i></i>News feed</span>
      </div>
    </div>
  </div>
  <div class="copyright">© Vitoplume 2015 | All Rights Reserved | www.vitoplume.com</div>
</footer>

</body>
</html>
```